7 3/4 x 5 1/4 Annual Banquet Invitation

Design an invitation for our Chamber's annual banquet. It will be a single sided invitation 5 1/4" wide by 7 3/4" height that we will print in-house. Our logo is attached. The theme is "Serving Together". I was thinking of an image with two hands coming together in a handshake, perhaps intertwining our logo colors. This is just a thought. I am open for any suggestions! Text for the invitation should be as follows: The Board of Directors and Staff cordially invites you to attend the 64th Yearly Gathering & Micro-Trade Fair - Monday, January 22, 2018. 5:30 p.m. Social, 6:00 p.m. Dinner. Cedarvale Chapel, 4819 Harlan P. Moss Rd S, Maplebrook. Please RSVP by January 18, 2018.

Target Market(s)

This invitation will be printed and mailed to our membership.

Industry/Entity Type

Business Management

Colors
33a6d7
faa54b
0355a3
00a990

Requirements
Must have
• Event info as indentified above.
Nice to have
• Our Logo

```html
<!DOCTYPE html>
<html lang="en">
<head>
<meta charset="utf-8">
<title>Harborview Chamber — 64th Yearly Gathering Invitation</title>
<link rel="stylesheet" href="https://fonts.googleapis.com/css2?family=Playfair+Display:ital,wght@1,400&family=Playfair+Display+SC:wght@400;700&display=swap">
<style>
  :root {
    --backdrop: #d9c7bd;
    --card: #f4f0e2;
    --navy: #22398a;
    --brand-blue: #1f3fd6;
    --gold: #c8a758;
    --frame-line: #d8cfc3;
    --band: #d6c3b8;
    --photo-light: #c9b9a6;
    --photo-dark: #8f8171;
  }
  * { margin: 0; padding: 0; box-sizing: border-box; }
  html, body {
    width: 813px; height: 1200px; overflow: hidden;
    background: var(--backdrop);
  }
  .invitation {
    position: absolute; left: 35px; top: 33px;
    width: 743px; height: 1135px;
    background: var(--card);
    box-shadow: 0 4px 14px rgba(60, 40, 30, 0.35);
    overflow: hidden;
  }
  .hero-photo {
    position: absolute; left: 0; top: 0; width: 100%; height: 298px;
    background: linear-gradient(100deg, var(--photo-light) 0%, #b4a593 35%, var(--photo-dark) 55%, #b8a894 80%, var(--photo-light) 100%);
  }
  .hero-band {
    position: absolute; left: 0; top: 298px; width: 100%; height: 12px;
    background: var(--band);
  }
  .inner-frame {
    position: absolute; left: 19px; top: 23px; right: 18px; bottom: 21px;
    border: 1.5px solid var(--frame-line);
    pointer-events: none;
  }
  .chamber-name {
    position: absolute; left: 0; right: 0; top: 190px;
    text-align: center;
    font-family: "Playfair Display SC", serif;
    font-weight: 700;
    color: var(--brand-blue);
  }
  .chamber-name .line-main { display: block; font-size: 32px; line-height: 36px; }
  .chamber-name .line-sub { display: block; font-size: 17px; letter-spacing: 3px; line-height: 22px; }
  .sc-text {
    position: absolute; left: 0; right: 0;
    text-align: center;
    font-family: "Playfair Display SC", serif;
    color: var(--navy);
  }
  .welcome { top: 373px; font-size: 20px; line-height: 30px; font-weight: 400; }
  .edition { top: 520px; font-size: 22px; font-weight: 700; letter-spacing: 0.5px; }
  .event-title {
    position: absolute; left: 0; right: 0; top: 558px;
    text-align: center;
    font-family: "Playfair Display", serif;
    font-style: italic; font-weight: 400;
    font-size: 66px; line-height: 76px;
    color: var(--gold);
  }
  .schedule { top: 793px; font-size: 20px; line-height: 34px; font-weight: 700; }
  .venue { top: 929px; font-size: 20px; line-height: 35px; font-weight: 700; }
  .rsvp { top: 1044px; font-size: 16px; font-weight: 700; }
  .foot-tab {
    position: absolute; left: 226px; bottom: 0; width: 279px; height: 27px;
    background: var(--band);
  }
</style>
</head>
<body>
  <main class="invitation">
    <div class="hero-photo" role="img" aria-label="Sepia photograph of two business people shaking hands"></div>
    <div class="hero-band"></div>
    <div class="chamber-name">
      <span class="line-main">Harborview Chamber</span>
      <span class="line-sub">of Commerce &amp; Tourism</span>
    </div>

    <p class="sc-text welcome">The Board of Directors and Staff<br>cordially invites you to attend</p>
    <p class="sc-text edition">THE 64TH YEARLY</p>
    <h1 class="event-title">Gathering &amp;<br>Micro-Trade Fair</h1>

    <p class="sc-text schedule">Monday, January 22, 2018.<br>5:30 p.m. Social<br>6:00 p.m. Dinner.</p>
    <p class="sc-text venue">Cedarvale Chapel,<br>4819 Harlan P. Moss Rd S, Maplebrook.</p>
    <p class="sc-text rsvp">Please RSVP by January 18, 2018.</p>

    <div class="inner-frame"></div>
    <div class="foot-tab"></div>
  </main>
</body>
</html>
```